create a webpage for optometry practice

I'm looking to create a professional and elegant webpage for my practice. I prefer neutral earthy colors, but I am open to other ideas. I have included an image of my logo to be used in the process. This will be a page that will illustrate information about my practice and the kind of services we offer. I am in process of having the practice remodeled. So I don't have any photos of my practice to include yet.

Target Market(s)

My practice serves young and mature families.

Industry/Entity Type

It Professional

Number of Pages Required

5+ page

Font styles to use
Sans Serif

Colors
33a6d7
86cfc6
85cae6
cadf82
3276b5
faa54b
abd036
f78c1e

Requirements
Must have
• I would need to incorporate information about my practice, services, insurance accepted, make appointment, contact us, and about our family.
Nice to have
• I would like to see something fresh, modern, and unique

```html
<!DOCTYPE html>
<html lang="en">
<head>
<meta charset="utf-8">
<title>Lumera Eye Care</title>
<link href="https://fonts.googleapis.com/css2?family=Questrial&family=Open+Sans:wght@400;600;700&family=Great+Vibes&display=swap" rel="stylesheet">
<style>
:root{
  --teal:#7fcdc3;
  --sky:#85cae6;
  --sky-deep:#33a6d7;
  --orange:#f78c1e;
  --orange-soft:#faa54b;
  --green:#cadf82;
  --ink:#222;
  --text:#5a5a5a;
  --panel:#ececec;
  --hero-bg:#dde9f3;
  --white:#fff;
}
*{margin:0;padding:0;box-sizing:border-box}
html,body{width:1200px;height:2315px;overflow:hidden;background:var(--white)}
body{position:relative;font-family:"Open Sans",Arial,sans-serif;color:var(--text)}
.abs{position:absolute}

/* header */
.brand{left:73px;top:30px;display:flex;align-items:center;gap:10px}
.brand-dot{width:34px;height:34px;border-radius:50%;background:var(--teal)}
.brand-name{font-family:"Questrial",sans-serif;font-size:24px;color:#555;letter-spacing:1px;line-height:1}
.header-info{right:73px;top:28px;text-align:right;font-size:13px;color:#666}
.header-info .call{color:var(--orange);font-weight:700;font-size:12px}
.header-info .call span{color:#555;font-weight:400;font-size:13px}
.header-info .addr{margin-top:14px;font-size:12px;text-transform:uppercase}
.social{display:flex;gap:6px;justify-content:flex-end;margin-top:14px}
.social i{display:block;width:24px;height:24px;border-radius:50%;border:1.5px solid #aaa}

/* nav */
.nav{left:73px;top:143px;width:1052px;height:36px;background:var(--teal);display:flex;align-items:center;padding-left:36px}
.nav a{font-family:"Questrial",sans-serif;color:var(--white);font-size:13px;text-transform:uppercase;text-decoration:none;margin-right:46px;font-weight:700;letter-spacing:.3px}
.search{position:absolute;right:8px;top:5px;width:212px;height:26px;background:var(--white);font-size:12px;color:#999;padding:6px 8px}
.search svg{position:absolute;right:7px;top:6px}

/* hero */
.hero{left:73px;top:193px;width:1052px;height:488px;background:var(--hero-bg);overflow:hidden}
.hero-art{left:0;top:0;width:1052px;height:488px;background:
  radial-gradient(ellipse 42% 30% at 52% 48%,#d9b8a8 0%,#c9c9cf 55%,rgba(221,233,243,0) 100%),
  linear-gradient(180deg,#dde9f3 0%,#d6e6ee 50%,#e6dccf 100%)}
.hero-line{left:23px;font-family:"Questrial",sans-serif;color:#111;font-size:36px;line-height:1}
.hero-line b{font-weight:700;font-family:"Open Sans",sans-serif;font-size:33px}
.hero-line em{font-family:"Great Vibes",cursive;font-style:normal;color:var(--orange);font-size:38px}
.dots{right:26px;bottom:30px;display:flex;gap:3px}
.dots i{width:9px;height:9px;border:1px solid #999;background:#f3f3f3}
.dots i.on{background:#888}

/* welcome */
.h2{font-family:"Questrial",sans-serif;color:var(--ink);font-size:24px;font-weight:700}
.welcome{left:73px;top:718px;width:360px}
.para{font-size:12.5px;line-height:24px;color:var(--text)}
.welcome .para{margin-top:12px}
.btn-outline{display:inline-block;margin-top:20px;border:1.5px solid var(--teal);color:var(--teal);font-size:12px;padding:7px 14px;text-transform:uppercase;font-family:"Questrial",sans-serif}

.card{top:720px;width:211px;height:249px;color:var(--white);text-align:center;padding:26px 22px 0}
.card h3{font-family:"Questrial",sans-serif;font-size:17px;margin-top:16px;text-transform:uppercase}
.card p{font-size:11.5px;line-height:21px;margin-top:8px}
.card.exam{left:471px;background:var(--sky)}
.card.lens{left:691px;background:var(--orange-soft)}
.card.lasik{left:913px;background:var(--green)}

/* appointment */
.appt{left:73px;top:1034px;width:334px;height:566px;background:var(--panel)}
.appt-head{height:105px;background:var(--sky);color:var(--white);text-align:center;padding-top:14px}
.appt-head h2{font-family:"Questrial",sans-serif;font-size:24px;font-weight:700}
.appt-head .phone{display:flex;justify-content:center;align-items:center;gap:8px;font-size:24px;margin-top:4px;font-family:"Questrial",sans-serif}
.phone-dot{width:30px;height:30px;border-radius:50%;background:var(--sky-deep);display:flex;align-items:center;justify-content:center}
.or{position:absolute;left:150px;top:89px;width:32px;height:32px;border-radius:50%;background:var(--orange);border:3px solid var(--white);color:var(--white);font-size:10px;font-weight:700;text-align:center;line-height:26px}
.field{position:absolute;left:27px;width:278px;height:32px;background:var(--white);border:1px solid #dedede;font-size:12px;color:#999;padding:8px 10px}
.field.msg{height:114px}
.field.code{width:120px}
.captcha{position:absolute;left:162px;top:458px;width:85px;height:33px;background:#fff7ee;color:var(--orange);font-size:18px;font-family:"Questrial",sans-serif;text-align:center;line-height:33px;letter-spacing:1px}
.btn-solid{position:absolute;left:27px;top:504px;width:139px;height:33px;background:var(--orange);color:var(--white);font-size:12px;font-weight:700;text-transform:uppercase;text-align:center;line-height:33px;font-family:"Questrial",sans-serif}

.doctor{left:444px;top:1034px;width:681px;height:400px;background:radial-gradient(ellipse at 62% 45%,#c9ced3 0%,#e6e9ec 38%,#f7f8f9 62%,#fff 80%)}
.practice{left:434px;top:1440px;width:691px}
.practice .para{margin-top:16px}

/* testimonial */
.testimonials{left:73px;top:1648px}
.avatar{left:85px;top:1698px;width:111px;height:111px;border-radius:50%;background:radial-gradient(circle at 50% 40%,#d7c2b0,#8aa3b8);border:4px solid #e8e8e8}
.quote-mark{left:226px;top:1690px;font-size:60px;color:#bbb;font-family:Georgia,serif;line-height:1}
.quote{left:260px;top:1702px;width:865px}
.author{left:260px;top:1845px;color:var(--orange);font-size:12px;font-weight:700}
.t-dots{left:130px;top:1848px;display:flex;gap:4px}
.t-dots i{width:10px;height:10px;border-radius:50%;background:#ddd}
.t-dots i.on{background:var(--teal)}

/* newsletter */
.newsletter{left:0;top:1914px;width:1200px;height:93px;background:var(--teal)}
.nl-title{left:155px;top:24px;color:var(--white);font-family:"Questrial",sans-serif;font-size:19px;font-weight:700;line-height:20px;text-transform:uppercase}
.nl-input{left:343px;top:31px;width:300px;height:32px;background:var(--white);font-size:12px;color:#999;padding:9px 10px}
.nl-btn{left:651px;top:31px;width:110px;height:32px;background:var(--orange);color:var(--white);font-size:12px;font-weight:700;text-align:center;line-height:32px;text-transform:uppercase;font-family:"Questrial",sans-serif}
.stay{left:883px;top:24px}
.nl-social{left:1024px;top:35px;display:flex;gap:6px}
.nl-social i{width:25px;height:25px;border-radius:50%;border:1.5px solid var(--white)}

/* footer */
.footer{left:0;top:2007px;width:1200px;height:308px;background:var(--panel)}
.col{top:2050px;width:240px}
.col h4{font-family:"Questrial",sans-serif;font-size:13px;color:var(--ink);font-weight:700;text-transform:uppercase}
.post{margin-top:22px;font-size:11px;color:#777}
.post p{margin-top:6px;font-size:13px;line-height:17px;color:#666}
.contact-row{display:flex;gap:14px;margin-top:18px;font-size:12.5px;color:#666;line-height:17px}
.c-icon{flex:none;width:32px;height:32px;border-radius:50%;background:#444;display:flex;align-items:center;justify-content:center}
.foot-brand{left:884px;top:2080px;display:flex;align-items:center;gap:8px}
.foot-brand .brand-dot{width:26px;height:26px}
.foot-brand .brand-name{font-size:20px}
.copy{left:884px;top:2190px;font-size:12.5px;color:#555;line-height:19px}
</style>
</head>
<body>

<header>
  <div class="abs brand">
    <span class="brand-dot"></span>
    <span class="brand-name">LUMERA EYE CARE</span>
  </div>
  <div class="abs header-info">
    <div class="call">CALL US DIRECTLY : <span>1-800-555-0142</span></div>
    <div class="addr">228, Lorem Ipsum, Dolor sit, 898585-Lorem</div>
    <div class="social"><i></i><i></i><i></i></div>
  </div>
</header>

<nav class="abs nav">
  <a>Home</a><a>About Us</a><a>Services</a><a>Our Practice</a><a>Appointments</a><a>Blog</a><a>Contact Us</a>
  <div class="search">Enter Your Search
    <svg width="13" height="13" viewBox="0 0 13 13"><circle cx="5.5" cy="5.5" r="4.3" fill="none" stroke="#7fcdc3" stroke-width="1.6"/><path d="M8.6 8.6l3.5 3.5" stroke="#7fcdc3" stroke-width="1.8"/></svg>
  </div>
</nav>

<section class="abs hero">
  <div class="abs hero-art" role="img" aria-label="Banner illustration of a close-up eye framed by coloured sweeping curves"></div>
  <div class="abs hero-line" style="top:388px">BETTER <b>VISION</b> <em>for</em></div>
  <div class="abs hero-line" style="top:426px;left:108px">A BETTER <b>LIFE</b></div>
  <div class="abs dots"><i class="on"></i><i></i><i></i><i></i><i></i></div>
</section>

<section class="abs welcome">
  <h2 class="h2">Welcome to Lumera Eyecare</h2>
  <p class="para">In publishing and graphic design, lorem ipsum is a filler text commonly used to demonstrate the graphic elements of a document or visual presentation. Replacing meaningful content with placeholder commonly used to demonstrate text allows commonly used to view quickly-generated intoo ic elements of acommonly used to demonstrate document or visual presentation.</p>
  <span class="btn-outline">Read More</span>
</section>

<article class="abs card exam">
  <svg width="90" height="70" viewBox="0 0 90 70"><g fill="none" stroke="#fff" stroke-width="4"><circle cx="24" cy="40" r="17"/><circle cx="66" cy="40" r="17"/><path d="M38 22h14M45 6v16"/></g><circle cx="24" cy="40" r="6" fill="#fff"/><circle cx="66" cy="40" r="6" fill="#fff"/></svg>
  <h3>Eye Exams</h3>
  <p>In publishing and graphic design, lorem ipsum is a filler text or visual presentation.</p>
</article>
<article class="abs card lens">
  <svg width="90" height="70" viewBox="0 0 90 70"><g fill="none" stroke="#fff" stroke-width="5"><ellipse cx="35" cy="38" rx="26" ry="16"/><path d="M40 20 C70 10 88 30 70 48"/></g></svg>
  <h3>Contact Lenses</h3>
  <p>In publishing and graphic design, lorem ipsum is a filler text or visual presentation.</p>
</article>
<article class="abs card lasik">
  <svg width="100" height="70" viewBox="0 0 100 70"><path d="M6 38 C30 10 70 10 94 38 C70 62 30 62 6 38Z" fill="none" stroke="#fff" stroke-width="4"/><circle cx="50" cy="38" r="13" fill="#fff"/><path d="M20 20 C40 4 62 4 80 18" fill="none" stroke="#fff" stroke-width="4"/></svg>
  <h3>Lasik</h3>
  <p>In publishing and graphic design, lorem ipsum is a filler text or visual presentation.</p>
</article>

<aside class="abs appt">
  <div class="appt-head">
    <h2>Make an Appointment</h2>
    <div class="phone"><span class="phone-dot"><svg width="12" height="16" viewBox="0 0 12 16"><rect x="1" y="1" width="10" height="14" rx="2" fill="none" stroke="#fff" stroke-width="1.8"/><circle cx="6" cy="12" r="1.2" fill="#fff"/></svg></span>1-800-555-0142</div>
  </div>
  <div class="or">OR</div>
  <div class="field" style="top:139px">Full Name</div>
  <div class="field" style="top:186px">Phone Number</div>
  <div class="field" style="top:234px">Email Address</div>
  <div class="field" style="top:280px">Appointment Date</div>
  <div class="field msg" style="top:328px">Message</div>
  <div class="field code" style="top:458px">Enter Code</div>
  <div class="captcha">mmehx</div>
  <div class="btn-solid">Submit Request</div>
</aside>

<div class="abs doctor" role="img" aria-label="Photograph of an optometrist in glasses holding a tablet in the exam room"></div>
<section class="abs practice">
  <h2 class="h2">About My Practice</h2>
  <p class="para">In publishing and graphic design, lorem ipsum is a filler text commonly used to demonstrate the graphic elements of a document or visual presentation. Replacing meaningful content with placeholder commonly used to demonstrate text allows commonly used to view quickly-generated intoo ic elements of acommonly used to demonstrate document or visual presentation.</p>
</section>

<h2 class="abs h2 testimonials">What Our Patients Say</h2>
<div class="abs avatar" role="img" aria-label="Portrait photograph of a smiling patient"></div>
<div class="abs quote-mark">&ldquo;</div>
<div class="abs quote"><p class="para">In publishing and graphic design, lorem ipsum is a filler text commonly used to demonstrate the graphic elements of a document or visual presentation. Replacing meaningful content with placeholder commonly used to demonstrate text allows commonly used to view quickly-generated intoo ic elements of acommonly used to demonstrate document or visual presentation. In publishing and graphic design, lorem ipsum is a filler text commonly used to demonstrate the graphic elements of a document or visual presentation. Replacing meaningful content with place commonly used to view quickly-generated intoo ic elements of acommonly used to demonstrate document or visual presentation.</p></div>
<div class="abs t-dots"><i class="on"></i><i></i><i></i></div>
<div class="abs author">- Daniel Marsh</div>

<section class="abs newsletter">
  <svg class="abs" style="left:72px;top:26px" width="72" height="42" viewBox="0 0 72 42"><g fill="none" stroke="#fff" stroke-width="2.5"><path d="M22 6h46v30H22z"/><path d="M22 6l23 17 23-17"/><path d="M2 14h14M6 22h10M2 30h14"/></g></svg>
  <div class="abs nl-title">Subscribe<br>Our Newsletter</div>
  <div class="abs nl-input">Enter Your Email</div>
  <div class="abs nl-btn">Subscribe</div>
  <div class="abs nl-title stay">Stay<br>Connected</div>
  <div class="abs nl-social"><i></i><i></i><i></i></div>
</section>

<footer class="abs footer"></footer>
<div class="abs col" style="left:73px">
  <h4>Recent Blog</h4>
  <div class="post">10 MAR 2015 | 10 Comments<p>Mirum est notare quam littera gothi ca, quam nunc</p></div>
  <div class="post" style="margin-top:40px">10 MAR 2015 | 10 Comments<p>Mirum est notare quam littera gothi ca, quam nunc</p></div>
</div>
<div class="abs col" style="left:343px">
  <h4>Recent News</h4>
  <div class="post">10 MAR 2015<p>Mirum est notare quam littera gothi ca, quam nunc</p></div>
  <div class="post" style="margin-top:40px">10 MAR 2015<p>Mirum est notare quam littera gothi ca, quam nunc</p></div>
</div>
<div class="abs col" style="left:614px">
  <h4>Get In Touch</h4>
  <div class="contact-row"><span class="c-icon"><svg width="12" height="16" viewBox="0 0 12 16"><path d="M6 15C2 10 1 8 1 6a5 5 0 0110 0c0 2-1 4-5 9z" fill="#fff"/><circle cx="6" cy="6" r="2" fill="#444"/></svg></span><span>228, Lorem Ipsum,<br>Dolor sit, 898585-Lorem</span></div>
  <div class="contact-row"><span class="c-icon"><svg width="14" height="14" viewBox="0 0 14 14"><path d="M3 1l3 3-2 2c1 2 2 3 4 4l2-2 3 3-2 2C6 13 1 8 1 3z" fill="#fff"/></svg></span><span>Phone :<br>1-800-555-0142</span></div>
  <div class="contact-row"><span class="c-icon"><svg width="14" height="11" viewBox="0 0 14 11"><rect x="1" y="1" width="12" height="9" fill="#fff"/><path d="M1 1l6 5 6-5" fill="none" stroke="#444" stroke-width="1.2"/></svg></span><span>Email :<br>info@lumeraeyecare.com</span></div>
</div>
<div class="abs foot-brand"><span class="brand-dot"></span><span class="brand-name">LUMERA EYE CARE</span></div>
<div class="abs copy">© 2015 Lumera Eye Care.<br>All Rights Reserved. Terms &amp; Conditions<br>Privacy Policy | Terms of Use</div>

</body>
</html>
```